Vantor Advisory business card

Premium business card required
I have attached the brand as a powerpoint template but this can be made to look very up market, I have also attached my BIO for title reasons and to give you a feel for my skills
front of card
Derek Holloway
Managing Director Vantor Advisory
Retail, Customer-Led Experience, Transformation and Maximising Shareholder Return
Mobile +61(0)418557392
Email derekvantoradvisory.com
back of card

VANTOR ADVISORY’ OFFERING

We transform customer environments to extract benefits while elevating service levels;
We release millions of dollars in self-funding through continuous improvement;
We see CX as a key differentiator, proactively guarding share from market disrupters;
We re-invent service and create front-end of the future.

```html
<!DOCTYPE html>
<html lang="en">
<head>
<meta charset="utf-8">
<title>Vantor Advisory business card</title>
<link rel="stylesheet" href="https://fonts.googleapis.com/css2?family=Roboto:wght@400;500&family=Roboto+Condensed:wght@500;700&display=swap">
<style>
  :root {
    --stage: #2b2b2b;
    --card-light: #f4f4f2;
    --card-dark-top: #5e5e5e;
    --card-dark-bottom: #505050;
    --ink: #4a4a4a;
    --ink-strong: #555555;
    --gold: #c6a32c;
    --white: #ffffff;
    --rule: #a8a8a8;
  }
  * { margin: 0; padding: 0; box-sizing: border-box; }
  html, body { width: 1200px; height: 960px; overflow: hidden; }
  body { background: var(--stage); position: relative; font-family: "Roboto", Arial, sans-serif; }

  .card { position: absolute; width: 600px; height: 343px; }
  .card-front { left: 314px; top: 113px; background: var(--card-light); }
  .card-back { left: 311px; top: 472px; background: linear-gradient(180deg, var(--card-dark-top), var(--card-dark-bottom)); }

  .brand { position: absolute; display: flex; align-items: center; gap: 12px; font-family: "Roboto", Arial, sans-serif; font-weight: 500; white-space: nowrap; }
  .brand-dot { border-radius: 50%; flex: none; }
  .card-front .brand { right: 36px; top: 46px; font-size: 34px; color: var(--ink-strong); }
  .card-front .brand-dot { width: 40px; height: 40px; background: var(--ink-strong); }
  .card-back .brand { left: 0; right: 0; justify-content: center; top: 70px; font-size: 52px; color: var(--white); }
  .card-back .brand-dot { width: 62px; height: 62px; background: var(--white); }

  .holder { position: absolute; left: 36px; top: 156px; }
  .holder-name { font-family: "Roboto Condensed", Arial, sans-serif; font-weight: 700; font-size: 22px; color: var(--gold); letter-spacing: 0.2px; line-height: 1; }
  .holder-title { margin-top: 6px; font-size: 14.5px; line-height: 18px; color: var(--ink); }

  .divider { position: absolute; left: 36px; width: 528px; top: 242px; height: 1px; background: var(--rule); }

  .contacts { position: absolute; left: 36px; top: 252px; list-style: none; }
  .contacts li { display: flex; align-items: center; gap: 8px; font-size: 14.5px; line-height: 19px; color: var(--ink); }
  .contacts svg { width: 13px; height: 13px; fill: var(--gold); flex: none; }

  .offering { position: absolute; left: 0; right: 0; top: 222px; text-align: center; color: var(--white); }
  .offering-heading { display: flex; align-items: center; justify-content: center; gap: 4px; font-family: "Roboto Condensed", Arial, sans-serif; font-weight: 700; font-size: 18px; color: var(--gold); line-height: 1; }
  .offering-heading::before, .offering-heading::after { content: ""; width: 112px; height: 1px; background: var(--white); }
  .offering-list { margin-top: 6px; list-style: none; font-size: 12.2px; line-height: 15.5px; }
</style>
</head>
<body>
  <section class="card card-front" aria-label="Business card front">
    <div class="brand"><span>Vantor Advisory</span><span class="brand-dot"></span></div>
    <div class="holder">
      <h1 class="holder-name">DEREK HOLLOWAY</h1>
      <p class="holder-title">Managing Director Vantor Advisory<br>Retail, Customer-Led Experience<br>Transformation &amp; Maximising Shareholder Return</p>
    </div>
    <div class="divider"></div>
    <ul class="contacts">
      <li><svg viewBox="0 0 13 13" aria-hidden="true"><path d="M3 0h7a1 1 0 0 1 1 1v11a1 1 0 0 1-1 1H3a1 1 0 0 1-1-1V1a1 1 0 0 1 1-1zm.6 1.5v8.5h5.8V1.5zM6.5 10.6a.8.8 0 1 0 0 1.6.8.8 0 0 0 0-1.6z"/></svg>+61(0)418557392</li>
      <li><svg viewBox="0 0 13 13" aria-hidden="true"><path d="M0 3h13v1L6.5 8 0 4zm0 2.2 6.5 4 6.5-4V11H0z"/></svg>dh@derekvantoradvisory.com</li>
      <li><svg viewBox="0 0 13 13" aria-hidden="true"><circle cx="6.5" cy="6.5" r="6.2"/></svg>derekvantoradvisory.com</li>
    </ul>
  </section>

  <section class="card card-back" aria-label="Business card back">
    <div class="brand"><span>Vantor Advisory</span><span class="brand-dot"></span></div>
    <div class="offering">
      <h2 class="offering-heading">VANTOR ADVISORY’ OFFERING</h2>
      <ul class="offering-list">
        <li>We transform customer environments to extract benefits while elevating service levels;</li>
        <li>We release millions of dollars in self-funding through continuous improvement;</li>
        <li>We see CX as a key differentiator, proactively guarding share from market disrupters;</li>
        <li>We re-invent service and create front-end of the future.</li>
      </ul>
    </div>
  </section>
</body>
</html>
```